Zielgruppe
Massagen und Therapien an Patienten mit Schmerzen an Muskeln und am gesamten Bewegungsapparat. Nachbehandlung nach Operationen und Verletzungen sowie Sportverletzungen therapieren.
Zielgruppe: alle Personen (m/w) jeden alters egal ob sportlich oder 'faul'.
Aufgabenstellung
Das Design soll Ruhe, Harmonie, Vertrautheit und Geborgenheit vermitteln. Es muß mit dem Firmenlogo harmonisieren (Farbe und Gestaltung).
Das Logo und der Text findet sich im Anhang.
Es können Bilder eigenständig hinzugefügt werden.
Unbedingt DIN-Format verwenden (welches bleibt dem Designer überlassen)

```html
<!DOCTYPE html>
<html lang="de">
<head>
<meta charset="utf-8">
<title>Massagepraxis – Leistungen</title>
<link href="https://fonts.googleapis.com/css2?family=Source+Sans+3:wght@300;400;700&display=swap" rel="stylesheet">
<style>
  :root {
    --ink: #1f1f1f;
    --wave-blue: #1e9ad6;
    --green-light: #f6f9f0;
    --green-mid: #cfe3ad;
    --green-deep: #86bb45;
    --photo-skin: #e2b99a;
    --photo-white: #f2f1ef;
    --photo-grey: #8d8d8d;
    --photo-dark: #2a2a2a;
  }
  * { margin: 0; padding: 0; box-sizing: border-box; }
  html, body { width: 1200px; height: 1139px; overflow: hidden; background: #fff; }
  .flyer {
    position: relative; width: 1200px; height: 1139px; overflow: hidden;
    font-family: "Source Sans 3", "Myriad Pro", Arial, sans-serif; color: var(--ink);
  }
  .backdrop { position: absolute; inset: 0; }
  .photo { position: absolute; }
  .photo-lymph { left: 0; top: 0; width: 393px; height: 620px; background: linear-gradient(160deg, var(--photo-white) 0%, #e8ddd3 45%, var(--photo-skin) 100%); }
  .photo-acupoint { left: 397px; top: 0; width: 402px; height: 342px; background: linear-gradient(135deg, #f3ddc9 0%, var(--photo-skin) 60%, #c99474 100%); }
  .photo-headache { left: 397px; top: 345px; width: 402px; height: 300px; background: radial-gradient(ellipse at 50% 45%, #d9b49b 0%, #a58c7e 45%, var(--photo-grey) 100%); }
  .photo-ems { left: 803px; top: 0; width: 397px; height: 600px; background: linear-gradient(180deg, var(--photo-white) 0%, #e7e7e7 40%, #6a6a6a 75%, var(--photo-dark) 100%); }
  .panel { position: absolute; font-size: 15px; line-height: 19.6px; }
  .panel-title { font-weight: 400; font-size: 28px; line-height: 36px; }
  .panel ul { list-style: none; }
  .panel li::before { content: "• "; }
  .label { font-weight: 700; font-size: 17px; line-height: 20px; margin-top: 18px; }
  .col-lymph { left: 30px; top: 586px; width: 350px; }
  .col-lymph .panel-title { margin-left: 66px; margin-bottom: 34px; }
  .col-acu { left: 421px; top: 666px; width: 370px; }
  .col-acu .panel-title { text-align: center; margin-left: -20px; margin-bottom: 32px; }
  .col-ems { left: 827px; top: 612px; width: 360px; }
  .col-ems .panel-title { margin-left: 10px; margin-bottom: 48px; }
  .highlight { text-align: center; font-weight: 700; font-size: 23px; line-height: 28px; margin: 26px 0 32px 0; }
  .gap { height: 34px; }
</style>
</head>
<body>
<div class="flyer">
  <div class="photo photo-lymph" role="img" aria-label="Foto: Hände bei einer sanften Lymphdrainage am Rücken"></div>
  <div class="photo photo-acupoint" role="img" aria-label="Foto: Therapeut zeichnet Meridianlinien auf einen Rücken"></div>
  <div class="photo photo-headache" role="img" aria-label="Foto: Frau mit Kopfschmerzen hält sich die Schläfen"></div>
  <div class="photo photo-ems" role="img" aria-label="Foto: Mann im EMS-Anzug beim Ganzkörpertraining"></div>

  <svg class="backdrop" width="1200" height="1139" viewBox="0 0 1200 1139" aria-hidden="true">
    <defs>
      <linearGradient id="green-field" x1="0" y1="0" x2="0" y2="1">
        <stop offset="0" stop-color="var(--green-light)"/>
        <stop offset="0.45" stop-color="var(--green-mid)"/>
        <stop offset="1" stop-color="var(--green-deep)"/>
      </linearGradient>
    </defs>
    <path d="M0 598 C40 560 90 532 160 538 C300 552 420 640 600 638 C760 636 840 545 960 536 C1060 530 1140 545 1200 548 L1200 1139 L0 1139 Z" fill="url(#green-field)"/>
    <path d="M0 606 C40 570 90 544 160 550 C300 562 420 650 600 648 C760 646 840 556 960 547 C1060 541 1140 556 1200 559" fill="none" stroke="#ffffff" stroke-width="6"/>
    <path d="M0 598 C40 560 90 532 160 538 C300 552 420 640 600 638 C760 636 840 545 960 536 C1060 530 1140 545 1200 548" fill="none" stroke="var(--wave-blue)" stroke-width="6"/>
  </svg>

  <section class="panel col-lymph">
    <h2 class="panel-title">Lymphdrainage</h2>
    <p>Die sanften, schmerzfreien und&nbsp; langsam<br>ausgeführten Griffe wirken</p>
    <ul style="margin-top:19px">
      <li>Entwässernd —&gt;&nbsp; entstauend</li>
      <li>Entgiftend —&gt; entschlakend</li>
      <li>Beruhigend —&gt; entspannend</li>
      <li>stärken das Immunsystem</li>
      <li>bei Rheumatische Schwellungen</li>
    </ul>
    <p class="label">Indikationen:</p>
    <ul>
      <li>nach Operationen</li>
      <li>nach Tumorbehandlungen</li>
      <li>nach Verletzungen</li>
      <li>nach&nbsp; Lymphknotenentfernungen</li>
      <li>nach Hämatomen (Bluterguß)</li>
      <li>hoher Muskeltonus</li>
    </ul>
    <p style="margin-top:36px">Über das Lymphsystem werden die meisten<br>Abfallprodukte des Körpers abtransportiert.</p>
  </section>

  <section class="panel col-acu">
    <h2 class="panel-title">Akupunk-Massage nach<br>Venholt</h2>
    <p>durch diese&nbsp; Behandlungsmethode können viele<br>Beschwerde- und Krankheitsbilder beeinflusst werden<br>die durch funktionelle Störungen im Körper verursacht<br>worden sind.</p>
    <p class="label" style="margin-top:50px">Indikationen:</p>
    <ul>
      <li>Wirbelsäulenbeschwerden</li>
      <li>Migräne</li>
      <li>Erkrankungen der Gelenke</li>
      <li>Neuralgien</li>
      <li>Durchblutungsstörungen</li>
      <li>u.v.m</li>
    </ul>
  </section>

  <section class="panel col-ems">
    <h2 class="panel-title">EMS-Ganzkörpertraining</h2>
    <p>EMS (Elektro-Muskel-Stimulation) ist eine neue<br>Dimension des Ganzkörpertraining.<br>Schneller und intensiver als mit herkömmlichen<br>Methoden, in weniger als</p>
    <p class="highlight">20 Minuten / Trainingseinheit<br>und<br>1x pro Woche.</p>
    <p>Dadurch kann effektiv und effizienter trainiert<br>werden, in allen Alters- und Leistungsstufen.</p>
    <ul style="margin-top:30px">
      <li>Gesundheit bedeutet Lebensqualität</li>
      <li>für einen Leistungsfähigen Körper</li>
      <li>Schlank &amp; Straff</li>
      <li>Fit im Sport</li>
    </ul>
  </section>
</div>
</body>
</html>
```